Computer Service Provider in Need of New Letterhead Design

We are Larkvale Computer Services, a computer/IT services company that provides IT Support, software, hardware, virus monitoring, etc. in Vermont. We are looking for new letterhead, that is both professional and matches the current theme of our business cards & website.
Please note that we want to include the following information:
www.Larkvale.example
802-555-0147
47 Fernwick Hollow Road, Williston, VT 05495
Reliable Support • Friendly Experts • Lasting Results
I will be attaching our logo along with the business card images.
We would love to have the

```html
<!DOCTYPE html>
<html lang="en">
<head>
<meta charset="utf-8">
<title>Larkvale Computer Services — Letterhead</title>
<link rel="stylesheet" href="https://fonts.googleapis.com/css2?family=Open+Sans:wght@400;600;700&display=swap">
<style>
  :root {
    --backdrop: #8c8c8c;
    --paper: #ffffff;
    --brand-blue: #2a5b84;
    --divider: #9a9a9a;
    --ink: #3a3a3a;
    --tagline-ink: #2b2b2b;
  }
  * { margin: 0; padding: 0; box-sizing: border-box; }
  html, body {
    width: 943px;
    height: 1200px;
    overflow: hidden;
    background: var(--backdrop);
    font-family: "Open Sans", Arial, sans-serif;
  }
  .canvas { position: relative; width: 943px; height: 1200px; }
  .letterhead {
    position: absolute;
    left: 74px; top: 102px;
    width: 775px; height: 1037px;
    background: var(--paper);
  }
  .wordmark {
    position: absolute;
    left: 72px; top: 88px;
    color: var(--brand-blue);
    font-weight: 700;
    line-height: 1;
  }
  .wordmark-name { display: block; font-size: 32px; letter-spacing: 0.2px; }
  .wordmark-sub { display: block; font-size: 15px; letter-spacing: 1.9px; margin-top: 3px; }
  .divider {
    position: absolute;
    width: 1px; height: 48px;
    top: 88px;
    background: var(--divider);
  }
  .divider-first { left: 301px; }
  .divider-second { left: 488px; }
  .address {
    position: absolute;
    left: 310px; top: 103px;
    width: 170px;
    text-align: center;
    font-size: 10.5px;
    line-height: 13.5px;
    letter-spacing: 1px;
    color: var(--ink);
    font-style: normal;
  }
  .contact-list {
    position: absolute;
    left: 514px; top: 91px;
    list-style: none;
    font-size: 10.5px;
    letter-spacing: 0.8px;
    color: var(--ink);
  }
  .contact-item { display: flex; align-items: center; height: 16px; }
  .contact-icon { width: 10px; height: 10px; margin-right: 8px; fill: var(--brand-blue); }
  .footer-band {
    position: absolute;
    left: 0; top: 958px;
    width: 671px; height: 7px;
    background: var(--brand-blue);
  }
  .footer-mark {
    position: absolute;
    left: 684px; top: 944px;
    width: 49px; height: 33px;
    background: var(--brand-blue);
  }
  .tagline {
    position: absolute;
    left: 0; top: 985px;
    width: 740px;
    text-align: center;
    font-size: 10.5px;
    font-weight: 700;
    letter-spacing: 1.3px;
    color: var(--tagline-ink);
  }
</style>
</head>
<body>
<div class="canvas">
  <section class="letterhead">
    <header>
      <div class="wordmark">
        <span class="wordmark-name">Larkvale</span>
        <span class="wordmark-sub">COMPUTER SERVICES</span>
      </div>
      <div class="divider divider-first"></div>
      <address class="address">47 Fernwick Hollow Road,<br>Brookmere, VT 05999</address>
      <div class="divider divider-second"></div>
      <ul class="contact-list">
        <li class="contact-item">
          <svg class="contact-icon" viewBox="0 0 10 10" aria-hidden="true"><path d="M2 0.5 L3.6 2.6 L2.7 3.6 C3.3 5 4.8 6.6 6.4 7.3 L7.4 6.4 L9.5 8 L8.3 9.5 C4.5 9.3 0.7 5.5 0.5 1.7 Z"/></svg>
          802-555-0147
        </li>
        <li class="contact-item">
          <svg class="contact-icon" viewBox="0 0 10 10" aria-hidden="true"><path d="M0.5 2 H9.5 V8 H0.5 Z"/><path d="M0.5 2 L5 5.5 L9.5 2" fill="none" stroke="#fff" stroke-width="0.9"/></svg>
          info@Larkvale.example
        </li>
        <li class="contact-item">
          <svg class="contact-icon" viewBox="0 0 10 10" aria-hidden="true"><circle cx="5" cy="5" r="4.5"/><path d="M1 5 H9 M5 0.8 C3 3 3 7 5 9.2 M5 0.8 C7 3 7 7 5 9.2" fill="none" stroke="#fff" stroke-width="0.6"/></svg>
          www.Larkvale.example
        </li>
      </ul>
    </header>
    <footer>
      <div class="footer-band"></div>
      <div class="footer-mark"></div>
      <p class="tagline">RELIABLE SUPPORT • FRIENDLY EXPERTS • LASTING RESULTS</p>
    </footer>
  </section>
</div>
</body>
</html>
```